Road Construction Company needs business cards

We would like a new business card designed for our business.

We're a road construction company based in Qld, Australia.

Can the business card please have the following information on it.

Name: Brent Malvoy
Position: General Manager
Phone: 0471 592 304
Email: Brent.malvoy@quendix.com.au
Address: 87 Harrowgate Ave, Pindarra, QLD, 4000
Website: www.quendix.com.au

Visually we'd like the card to be professional and simple.

Attached is our logo.

Our website is www.quendix.com.au

Target Market(s)

Men aged 25-60

Contact Information for Business Card

As listed in project description

Font styles to use
Serif

Requirements
Must have
• Large logo on back of card

```html
<!DOCTYPE html>
<html lang="en">
<head>
<meta charset="utf-8">
<title>Quendix Road Construction – Business Card</title>
<link rel="stylesheet" href="https://fonts.googleapis.com/css2?family=Nunito+Sans:wght@400;600;800&display=swap">
<style>
  :root {
    --backdrop: #a3a3a3;
    --card: #ffffff;
    --ink: #111111;
    --brand-deep: #0b55a3;
    --brand-sky: #2ea6da;
    --on-brand: #ffffff;
  }
  * { box-sizing: border-box; margin: 0; padding: 0; }
  html, body {
    width: 1200px;
    height: 1200px;
    overflow: hidden;
    background: var(--backdrop);
    font-family: "Nunito Sans", sans-serif;
  }
  .canvas { position: relative; width: 1200px; height: 1200px; }
  .card {
    position: absolute;
    left: 156px;
    width: 888px;
    height: 519px;
    background: var(--card);
    box-shadow: 0 4px 10px rgba(0,0,0,0.25);
    overflow: hidden;
  }
  .card--front { top: 56px; }
  .card--back { top: 615px; }

  .wordmark {
    position: absolute;
    color: var(--brand-deep);
    font-weight: 800;
    letter-spacing: 2px;
    line-height: 1;
  }
  .card--front .wordmark { left: 64px; top: 76px; font-size: 62px; }
  .card--back .wordmark {
    left: 0; right: 0; top: 190px;
    text-align: center;
    font-size: 96px;
    letter-spacing: 4px;
  }

  .person { position: absolute; left: 64px; top: 222px; }
  .person__name {
    font-size: 39px;
    font-weight: 600;
    color: var(--ink);
    text-transform: uppercase;
    line-height: 1.1;
  }
  .person__role {
    margin-top: 6px;
    font-size: 21px;
    color: var(--ink);
  }

  .contacts {
    position: absolute;
    left: 62px;
    top: 350px;
    list-style: none;
  }
  .contacts__item {
    display: flex;
    align-items: center;
    height: 34.5px;
    font-size: 22px;
    color: var(--ink);
  }
  .contacts__icon { width: 18px; height: 18px; margin-right: 12px; flex: none; }

  .accent-bar {
    position: absolute;
    left: 798px;
    top: 0;
    width: 55px;
    height: 394px;
    background: var(--brand-sky);
  }
  .web-band {
    position: absolute;
    left: 548px;
    top: 406px;
    width: 340px;
    height: 52px;
    background: var(--brand-deep);
    clip-path: polygon(15px 0, 100% 0, 100% 100%, 0 100%);
    display: flex;
    align-items: center;
    padding-left: 24px;
    color: var(--on-brand);
    font-size: 21px;
    font-weight: 600;
    letter-spacing: 0.3px;
  }
  .web-band svg { width: 18px; height: 18px; margin-right: 10px; }
</style>
</head>
<body>
<main class="canvas">
  <section class="card card--front" aria-label="Business card front">
    <div class="wordmark">QUENDIX</div>

    <div class="person">
      <h1 class="person__name">Brent Malvoy</h1>
      <p class="person__role">General Manager</p>
    </div>

    <ul class="contacts">
      <li class="contacts__item">
        <svg class="contacts__icon" viewBox="0 0 24 24" aria-hidden="true"><path fill="#111" d="M6.6 10.8a15.1 15.1 0 0 0 6.6 6.6l2.2-2.2a1 1 0 0 1 1-.25 11.4 11.4 0 0 0 3.6.57 1 1 0 0 1 1 1V20a1 1 0 0 1-1 1A17 17 0 0 1 3 4a1 1 0 0 1 1-1h3.5a1 1 0 0 1 1 1c0 1.25.2 2.45.57 3.57a1 1 0 0 1-.25 1z"/></svg>
        0471 592 304
      </li>
      <li class="contacts__item">
        <svg class="contacts__icon" viewBox="0 0 24 24" aria-hidden="true"><path fill="#111" d="M2 5h20v14H2z"/><path fill="none" stroke="#fff" stroke-width="1.8" d="M3 6l9 7 9-7"/></svg>
        Brent.malvoy@quendix.com.au
      </li>
      <li class="contacts__item">
        <svg class="contacts__icon" viewBox="0 0 24 24" aria-hidden="true"><path fill="#111" d="M12 1a7 7 0 0 0-7 7c0 5 7 12 7 12s7-7 7-12a7 7 0 0 0-7-7zm0 9.5A2.5 2.5 0 1 1 12 5.5a2.5 2.5 0 0 1 0 5z"/><rect x="4" y="21" width="16" height="2" fill="#111"/></svg>
        87 Harrowgate Ave, Pindarra, QLD, 4000
      </li>
    </ul>

    <div class="accent-bar"></div>
    <div class="web-band">
      <svg viewBox="0 0 24 24" aria-hidden="true"><circle cx="12" cy="12" r="10" fill="none" stroke="#fff" stroke-width="2"/><path fill="none" stroke="#fff" stroke-width="1.6" d="M2 12h20M12 2c3 3 3 17 0 20M12 2c-3 3-3 17 0 20"/></svg>
      www.quendix.com.au
    </div>
  </section>

  <section class="card card--back" aria-label="Business card back">
    <div class="wordmark">QUENDIX</div>
  </section>
</main>
</body>
</html>
```